Health Tech Company needs a better formated document for a customer project

Please use this excel spreadsheet and format a better looking word document to share with the customer.

```html
<!DOCTYPE html>
<html lang="en">
<head>
<meta charset="utf-8">
<title>Verellan – Escalation Code Reference, Typeface Options</title>
<link rel="stylesheet" href="https://fonts.googleapis.com/css2?family=Carlito:ital,wght@0,400;0,700;1,400;1,700&family=Noto+Sans:ital,wght@0,400;0,700;1,400;1,700&family=Open+Sans:ital,wght@0,400;0,700;1,400;1,700&family=Roboto+Condensed:wght@400&display=swap">
<style>
:root{
  --board:#c2c2c2;
  --paper:#ffffff;
  --band:#f4f4f4;
  --blue:#3b55a2;
  --rule:#b9c4e0;
  --ink:#555a60;
  --ink-soft:#6f7479;
  --brand-grey:#5d6268;
  --green:#7ab648;
  --yellow:#f7dd00;
  --gold:#e1c774;
  --teal:#3db5b0;
  --label:#2b2b2b;
}
*{box-sizing:border-box;margin:0;padding:0}
html,body{width:1200px;height:655px;overflow:hidden;background:var(--board)}
.board{position:relative;width:1200px;height:655px}
.option-label{position:absolute;top:78px;font-family:"Roboto Condensed",sans-serif;font-size:16px;letter-spacing:.3px;color:var(--label)}
.option{position:absolute;top:113px;width:325px;height:459px;overflow:hidden}
.page{width:596px;height:842px;background:var(--paper);transform:scale(.5455);transform-origin:0 0;position:relative;color:var(--ink)}
.font-calibri .page{font-family:"Carlito",sans-serif}
.font-tahoma .page{font-family:"Noto Sans",sans-serif}
.font-verdana .page{font-family:"Open Sans",sans-serif}

.page-head{height:100px;position:relative}
.brand{position:absolute;left:42px;top:36px;display:flex;align-items:center;gap:8px}
.brand-dot{width:24px;height:24px;border-radius:50%;background:var(--blue)}
.brand-name{font-size:30px;color:var(--brand-grey);font-weight:400;letter-spacing:.5px}
.tagline{position:absolute;left:224px;top:43px;font-size:10px;color:var(--ink)}
.tagline .url{display:block;font-size:8px;font-weight:700;color:var(--blue);margin-top:1px}
.page-no{position:absolute;left:553px;top:38px;font-size:10px;font-weight:700;color:var(--ink)}

.legend{background:var(--band);height:99px;padding:15px 42px 0}
.legend-title{font-size:8px;font-style:italic;color:#444;margin-bottom:6px}
.legend-items{display:flex;gap:8px}
.legend-item{width:122px;display:flex;gap:6px;font-size:5.4px;line-height:1.85;color:var(--ink)}
.legend-item i{font-style:italic;font-weight:700}
.swatch{flex:none;width:14px;height:14px;border-radius:50%;margin-top:3px}
.swatch.yellow{background:var(--yellow)}
.swatch.gold{background:var(--gold)}
.swatch.green{background:var(--green)}
.swatch.teal{background:var(--teal)}

.table-head{background:var(--blue);color:#fff;font-weight:700;font-size:6.6px;line-height:1.6;height:40px;display:grid;grid-template-columns:78px 149px 149px 1fr;padding:8px 42px 0 47px}
.rows{margin:0 36px 0 42px}
.row{display:grid;grid-template-columns:78px 149px 149px 1fr;padding:9px 0 9px 5px;border-bottom:1px solid var(--rule);font-size:6.3px;line-height:1.6}
.row > div{padding-right:10px}
.code{font-style:italic;font-weight:700;color:var(--ink-soft)}
.code b{display:block}
.mark{margin-top:7px;width:32px;height:32px;border-radius:50%;border:3px solid;display:flex;align-items:center;justify-content:center}
.mark::after{content:"";width:15px;height:15px;border-radius:50%;background:currentColor}
.mark.green{color:var(--green);border-color:var(--green)}
.mark.yellow{color:var(--yellow);border-color:var(--yellow)}
.rows-end{margin:1px 36px 0 42px;height:3px;background:var(--blue)}
</style>
</head>
<body>
<main class="board">

  <h2 class="option-label" style="left:80px">CALIBRI</h2>
  <h2 class="option-label" style="left:437px">TAHOMA</h2>
  <h2 class="option-label" style="left:793px">VERDANA</h2>

  <section class="option font-calibri" style="left:80px">
    <article class="page">
      <header class="page-head">
        <div class="brand"><span class="brand-dot"></span><span class="brand-name">verellan</span></div>
        <p class="tagline">Provider Engagement Solutions<span class="url">www.verellan.com</span></p>
        <span class="page-no">2</span>
      </header>
      <section class="legend">
        <p class="legend-title">COLOR LEGEND</p>
        <div class="legend-items">
          <p class="legend-item"><span class="swatch yellow"></span><span>Rows highlighted in <i>yellow</i> are provider removal reasons that can be used when a Research Analyst using the trashcan feature in the CRM</span></p>
          <p class="legend-item"><span class="swatch gold"></span><span>Rows highlighted in <i>gold</i> are used as both a provider removal reason and as a general escalation code in the CRM</span></p>
          <p class="legend-item"><span class="swatch green"></span><span>Rows highlighted in <i>green</i> are escalation codes that are not for removal and are instead used to share information with the health plan on their escalation report</span></p>
          <p class="legend-item"><span class="swatch teal"></span><span>Rows highlighted in <i>teal</i> are system escalations that happen as a result of an action taken by a Research Analyst in the CRM</span></p>
        </div>
      </section>
      <div class="table-head"><span>HPA SW Escalation Code</span><span>Reason This Code Is Used</span><span>Is rendering provider soft removed? (deactivated in the CRM) Y / N?</span><span>CRM- Verellan action required</span></div>
      <div class="rows">
        <div class="row"><div class="code"><b>Network Participation Question</b><span class="mark green"></span></div><div><i>A.</i> Escalation is done when clinic is unsure of network participation or has not heard of a specific plan (ie, Sky Path, HMO)</div><div>The providers information is still confirmed and marked as clean. Confirmed data will display on the weekly data extract and Network Participation question will be displayed on the weekly escalation report.</div><div>Mark as clean</div></div>
        <div class="row"><div class="code"><b>Confirmation Needed- Provider No Longer Practicing at TIN</b><span class="mark yellow"></span></div><div><i>A.</i> Contact at provider office has notified us that the provider is not practicing under TIN that AZ has provided to Verellan<br><i>B.</i> Contact at provider office or voicemail greeting has notified us that the provider has retired<br><i>C.</i> Contact at provider office has notified us that the provider deceased</div><div>Provider is soft removed from Verellan's CRM and removal is displayed on the weekly extract. Corresponding provider removal and available additional information are also displayed on the escalation report.</div><div>Utilize the trash can icon to successfully remove the provider. Select Confirmation Needed- Provider No longer Practicing at TIN as your reason code. Please include phone number, office contact's first name and job title in the activity stream comment section of the removal page.</div></div>
        <div class="row"><div class="code"><b>Office Closed- Confirmation Needed</b><span class="mark green"></span></div><div><i>A.</i> Office appears to be closed; obtained info via voicemail, online search, etc</div><div>Provider is not soft removed. Weekly extract report will show this provider group as cleaned, but not accepting new patients on the weekly extract. Office closed-Confirmation Needed will be listed on the weekly escalation report.</div><div>Switch toggle to NOT accepting new patients; Mark as clean</div></div>
        <div class="row"><div class="code"><b>Non-Participation</b><span class="mark green"></span></div><div>Contact at TIN states they are no longer participating with HPA SW Advantage or commercial plans</div><div>Provider is not soft removed. Weekly extract report will show this provider group as cleaned, but accepting new patients and Network participation will be showing as No on the weekly extract. "Medicaid or Medicare Non Participation" will be listed on the weekly escalation report.</div><div>Switch toggle to NOT accepting new patients; Mark as clean</div></div>
        <div class="row"><div class="code"><b>Practice Name Issue</b><span class="mark green"></span></div><div>Clinic is practicing under a new name</div><div>Unless, provider group declines to clean, the providers information is still confirmed and marked as clean. Confirmed data will display on the weekly data extract and Practice Name Issue will be displayed on the weekly escalation report.</div><div>Mark as clean, if the data was cleaned. Ask about the TIN, only clean if the TIN matches. If the TIN no longer matches, then use Not practicing under TIN and remove the providers.</div></div>
        <div class="row"><div class="code"><b>Other</b><span class="mark yellow"></span></div><div>Misc items where we do not have an existing Escalation bucket code: For example: Clinic is self pay only, office contact has unsubscribed from our webforms.</div><div>Details are only captured in the weekly escalation report</div><div>Dependent on what is being escalated</div></div>
      </div>
      <div class="rows-end"></div>
    </article>
  </section>

  <section class="option font-tahoma" style="left:437px">
    <article class="page">
      <header class="page-head">
        <div class="brand"><span class="brand-dot"></span><span class="brand-name">verellan</span></div>
        <p class="tagline">Provider Engagement Solutions<span class="url">www.verellan.com</span></p>
        <span class="page-no">2</span>
      </header>
      <section class="legend">
        <p class="legend-title">COLOR LEGEND</p>
        <div class="legend-items">
          <p class="legend-item"><span class="swatch yellow"></span><span>Rows highlighted in <i>yellow</i> are provider removal reasons that can be used when a Research Analyst using the trashcan feature in the CRM</span></p>
          <p class="legend-item"><span class="swatch gold"></span><span>Rows highlighted in <i>gold</i> are used as both a provider removal reason and as a general escalation code in the CRM</span></p>
          <p class="legend-item"><span class="swatch green"></span><span>Rows highlighted in <i>green</i> are escalation codes that are not for removal and are instead used to share information with the health plan on their escalation report</span></p>
          <p class="legend-item"><span class="swatch teal"></span><span>Rows highlighted in <i>teal</i> are system escalations that happen as a result of an action taken by a Research Analyst in the CRM</span></p>
        </div>
      </section>
      <div class="table-head"><span>HPA SW Escalation Code</span><span>Reason This Code Is Used</span><span>Is rendering provider soft removed? (deactivated in the CRM) Y / N?</span><span>CRM- Verellan action required</span></div>
      <div class="rows">
        <div class="row"><div class="code"><b>Network Participation Question</b><span class="mark green"></span></div><div><i>A.</i> Escalation is done when clinic is unsure of network participation or has not heard of a specific plan (ie, Sky Path, HMO)</div><div>The providers information is still confirmed and marked as clean. Confirmed data will display on the weekly data extract and Network Participation question will be displayed on the weekly escalation report.</div><div>Mark as clean</div></div>
        <div class="row"><div class="code"><b>Confirmation Needed- Provider No Longer Practicing at TIN</b><span class="mark yellow"></span></div><div><i>A.</i> Contact at provider office has notified us that the provider is not practicing under TIN that AZ has provided to Verellan<br><i>B.</i> Contact at provider office or voicemail greeting has notified us that the provider has retired<br><i>C.</i> Contact at provider office has notified us that the provider deceased</div><div>Provider is soft removed from Verellan's CRM and removal is displayed on the weekly extract. Corresponding provider removal and available additional information are also displayed on the escalation report.</div><div>Utilize the trash can icon to successfully remove the provider. Select Confirmation Needed- Provider No longer Practicing at TIN as your reason code. Please include phone number, office contact's first name and job title in the activity stream comment section of the removal page.</div></div>
        <div class="row"><div class="code"><b>Office Closed- Confirmation Needed</b><span class="mark green"></span></div><div><i>A.</i> Office appears to be closed; obtained info via voicemail, online search, etc</div><div>Provider is not soft removed. Weekly extract report will show this provider group as cleaned, but not accepting new patients on the weekly extract. Office closed-Confirmation Needed will be listed on the weekly escalation report.</div><div>Switch toggle to NOT accepting new patients; Mark as clean</div></div>
        <div class="row"><div class="code"><b>Non-Participation</b><span class="mark green"></span></div><div>Contact at TIN states they are no longer participating with HPA SW Advantage or commercial plans</div><div>Provider is not soft removed. Weekly extract report will show this provider group as cleaned, but accepting new patients and Network participation will be showing as No on the weekly extract. "Medicaid or Medicare Non Participation" will be listed on the weekly escalation report.</div><div>Switch toggle to NOT accepting new patients; Mark as clean</div></div>
        <div class="row"><div class="code"><b>Practice Name Issue</b><span class="mark green"></span></div><div>Clinic is practicing under a new name</div><div>Unless, provider group declines to clean, the providers information is still confirmed and marked as clean. Confirmed data will display on the weekly data extract and Practice Name Issue will be displayed on the weekly escalation report.</div><div>Mark as clean, if the data was cleaned. Ask about the TIN, only clean if the TIN matches. If the TIN no longer matches, then use Not practicing under TIN and remove the providers.</div></div>
        <div class="row"><div class="code"><b>Other</b><span class="mark yellow"></span></div><div>Misc items where we do not have an existing Escalation bucket code: For example: Clinic is self pay only, office contact has unsubscribed from our webforms.</div><div>Details are only captured in the weekly escalation report</div><div>Dependent on what is being escalated</div></div>
      </div>
      <div class="rows-end"></div>
    </article>
  </section>

  <section class="option font-verdana" style="left:795px">
    <article class="page">
      <header class="page-head">
        <div class="brand"><span class="brand-dot"></span><span class="brand-name">verellan</span></div>
        <p class="tagline">Provider Engagement Solutions<span class="url">www.verellan.com</span></p>
        <span class="page-no">2</span>
      </header>
      <section class="legend">
        <p class="legend-title">COLOR LEGEND</p>
        <div class="legend-items">
          <p class="legend-item"><span class="swatch yellow"></span><span>Rows highlighted in <i>yellow</i> are provider removal reasons that can be used when a Research Analyst using the trashcan feature in the CRM</span></p>
          <p class="legend-item"><span class="swatch gold"></span><span>Rows highlighted in <i>gold</i> are used as both a provider removal reason and as a general escalation code in the CRM</span></p>
          <p class="legend-item"><span class="swatch green"></span><span>Rows highlighted in <i>green</i> are escalation codes that are not for removal and are instead used to share information with the health plan on their escalation report</span></p>
          <p class="legend-item"><span class="swatch teal"></span><span>Rows highlighted in <i>teal</i> are system escalations that happen as a result of an action taken by a Research Analyst in the CRM</span></p>
        </div>
      </section>
      <div class="table-head"><span>HPA SW Escalation Code</span><span>Reason This Code Is Used</span><span>Is rendering provider soft removed? (deactivated in the CRM) Y / N?</span><span>CRM- Verellan action required</span></div>
      <div class="rows">
        <div class="row"><div class="code"><b>Network Participation Question</b><span class="mark green"></span></div><div><i>A.</i> Escalation is done when clinic is unsure of network participation or has not heard of a specific plan (ie, Sky Path, HMO)</div><div>The providers information is still confirmed and marked as clean. Confirmed data will display on the weekly data extract and Network Participation question will be displayed on the weekly escalation report.</div><div>Mark as clean</div></div>
        <div class="row"><div class="code"><b>Confirmation Needed- Provider No Longer Practicing at TIN</b><span class="mark yellow"></span></div><div><i>A.</i> Contact at provider office has notified us that the provider is not practicing under TIN that AZ has provided to Verellan<br><i>B.</i> Contact at provider office or voicemail greeting has notified us that the provider has retired<br><i>C.</i> Contact at provider office has notified us that the provider deceased</div><div>Provider is soft removed from Verellan's CRM and removal is displayed on the weekly extract. Corresponding provider removal and available additional information are also displayed on the escalation report.</div><div>Utilize the trash can icon to successfully remove the provider. Select Confirmation Needed- Provider No longer Practicing at TIN as your reason code. Please include phone number, office contact's first name and job title in the activity stream comment section of the removal page.</div></div>
        <div class="row"><div class="code"><b>Office Closed- Confirmation Needed</b><span class="mark green"></span></div><div><i>A.</i> Office appears to be closed; obtained info via voicemail, online search, etc</div><div>Provider is not soft removed. Weekly extract report will show this provider group as cleaned, but not accepting new patients on the weekly extract. Office closed-Confirmation Needed will be listed on the weekly escalation report.</div><div>Switch toggle to NOT accepting new patients; Mark as clean</div></div>
        <div class="row"><div class="code"><b>Non-Participation</b><span class="mark green"></span></div><div>Contact at TIN states they are no longer participating with HPA SW Advantage or commercial plans</div><div>Provider is not soft removed. Weekly extract report will show this provider group as cleaned, but accepting new patients and Network participation will be showing as No on the weekly extract. "Medicaid or Medicare Non Participation" will be listed on the weekly escalation report.</div><div>Switch toggle to NOT accepting new patients; Mark as clean</div></div>
        <div class="row"><div class="code"><b>Practice Name Issue</b><span class="mark green"></span></div><div>Clinic is practicing under a new name</div><div>Unless, provider group declines to clean, the providers information is still confirmed and marked as clean. Confirmed data will display on the weekly data extract and Practice Name Issue will be displayed on the weekly escalation report.</div><div>Mark as clean, if the data was cleaned. Ask about the TIN, only clean if the TIN matches. If the TIN no longer matches, then use Not practicing under TIN and remove the providers.</div></div>
        <div class="row"><div class="code"><b>Other</b><span class="mark yellow"></span></div><div>Misc items where we do not have an existing Escalation bucket code: For example: Clinic is self pay only, office contact has unsubscribed from our webforms.</div><div>Details are only captured in the weekly escalation report</div><div>Dependent on what is being escalated</div></div>
      </div>
      <div class="rows-end"></div>
    </article>
  </section>

</main>
</body>
</html>
```